Quick Straightforward Billboard Redesign

- Design billboard sized for 10 foot' x 36' foot width live area size and please include bleeds 6" around all sides
- Exact blue color match is imperative in headline, logo, phone number bubble or wherever used. C-83 / M-45 / Y-1 / K-0-
- What I hope to illustrate is that our company offers the best porch screening in the area area, in regards to quality, expertise, durability, storms proof, but we do not build screen porches.
- Current board is attached below from previous designer, and as you can see sizing was off, white space on edges make it appear to be sized incorrectly.
- I also attached my own little mock up idea well well if it helps, favorite image, logo, headline, etc and ideas perhaps on expanding or making this better?

Thanks so much!

Target Market(s)

Drivers and passengers, Southeastern NC, are of immense new construction and high end homes.

Industry/Entity Type

Construction

Colors
0054AA
0677BA
7BADD7
CADEEF
E8F1F8

Requirements
Must have
• Blue color matching
Nice to have
• Design spins or other thoughts on my little mock up

```html
<!DOCTYPE html>
<html lang="en">
<head>
<meta charset="utf-8">
<title>Tidewater Screening Billboard</title>
<link href="https://fonts.googleapis.com/css2?family=Oswald:wght@600;700&display=swap" rel="stylesheet">
<style>
  :root {
    --brand-blue: #0a6bb8;
    --brand-green: #0db45a;
    --paper: #ffffff;
    --stage: #3b3b3b;
    --photo-light: #eceeee;
    --photo-deep: #cdd1d3;
  }
  * { margin: 0; padding: 0; box-sizing: border-box; }
  html, body {
    width: 1200px;
    height: 432px;
    overflow: hidden;
    background: var(--stage);
  }
  .billboard {
    position: absolute;
    left: 0;
    top: 38px;
    width: 1200px;
    height: 356px;
    background: var(--paper);
    overflow: hidden;
    font-family: "Oswald", "Arial Narrow", sans-serif;
  }
  .billboard-art {
    position: absolute;
    inset: 0;
    width: 1200px;
    height: 356px;
  }
  .brand {
    position: absolute;
    left: 51px;
    top: 47px;
    display: flex;
    align-items: center;
    gap: 14px;
  }
  .brand-square {
    width: 36px;
    height: 36px;
    background: var(--brand-blue);
  }
  .brand-name {
    font-weight: 600;
    font-size: 51px;
    line-height: 1;
    color: var(--brand-blue);
    text-transform: uppercase;
    transform: scaleX(0.93);
    transform-origin: left center;
    white-space: nowrap;
  }
  .headline {
    position: absolute;
    left: 49px;
    top: 118px;
    font-weight: 700;
    font-size: 62px;
    line-height: 66px;
    text-transform: uppercase;
    transform: scaleX(0.975);
    transform-origin: left top;
  }
  .headline-line { display: block; white-space: nowrap; }
  .headline-line--blue { color: var(--brand-blue); word-spacing: 4px; }
  .headline-line--green { color: var(--brand-green); }
  .phone-bubble {
    position: absolute;
    left: 50px;
    top: 265px;
    width: 325px;
    height: 53px;
    background: var(--brand-blue);
    display: flex;
    align-items: center;
    padding-left: 13px;
    gap: 8px;
  }
  .phone-icon {
    width: 39px;
    height: 39px;
    background: var(--paper);
    border-radius: 7px;
    display: flex;
    align-items: center;
    justify-content: center;
  }
  .phone-number {
    color: var(--paper);
    font-weight: 700;
    font-size: 46px;
    line-height: 1;
    letter-spacing: 0.2px;
  }
</style>
</head>
<body>
  <section class="billboard">
    <svg class="billboard-art" viewBox="0 0 1200 356" xmlns="http://www.w3.org/2000/svg">
      <defs>
        <linearGradient id="photoTone" x1="0" y1="0" x2="0" y2="1">
          <stop offset="0" stop-color="#eceeee"/>
          <stop offset="1" stop-color="#cdd1d3"/>
        </linearGradient>
      </defs>
      <polygon class="stripe stripe--blue" fill="#0a6bb8"
        points="585,71 606,48 721,136 721,356 686,356 686,152"/>
      <polygon class="stripe stripe--green" fill="#0db45a"
        points="633,21 646,2 789,95 789,356 755,356 755,115"/>
      <polygon class="porch-photo" role="img"
        aria-label="Photo of a screened coastal porch with wicker seating, ceiling fans and a lake view"
        fill="url(#photoTone)"
        points="705,0 820,95 820,356 1200,356 1200,0"/>
    </svg>

    <div class="brand">
      <span class="brand-square"></span>
      <span class="brand-name">Tidewater Screening</span>
    </div>

    <h1 class="headline">
      <span class="headline-line headline-line--blue">Screen your porch.</span>
      <span class="headline-line headline-line--green">Build for the coast.</span>
    </h1>

    <div class="phone-bubble">
      <span class="phone-icon">
        <svg width="24" height="26" viewBox="0 0 24 26" xmlns="http://www.w3.org/2000/svg" aria-hidden="true">
          <path fill="#0a6bb8" d="M6 1 L9.5 1 L11 7 L8 9 C9 13 11 17 14 20 L17 18 L22 21 L21 25 C12 25 3 14 3 4 Z"/>
        </svg>
      </span>
      <span class="phone-number">910.555.0142</span>
    </div>
  </section>
</body>
</html>
```